Brisk Harbor Packaging Design for RTE Beans

We need a product mock design that is aligned with our brand image. We need three SKUs. Black bean, Pinto bean, and Chickpeas. I've uploaded our brand logo here, Brisk Harbor. I have also took a screenshot of the design elements that we would like to see. The packaging die line can be seen on the file "packaging sample". Please refer to the screenshots for packaging design directions.

```html
<!DOCTYPE html>
<html lang="en">
<head>
<meta charset="utf-8">
<title>Brisk Harbor – Ranger Black Beans Pouch</title>
<link href="https://fonts.googleapis.com/css2?family=Rye&family=Oswald:wght@400;500&display=swap" rel="stylesheet">
<style>
  :root {
    --backdrop: #6f673f;
    --pouch-light: #d9a23c;
    --pouch-mid: #b9772e;
    --pouch-dark: #7a4a22;
    --band: #2e2520;
    --gold: #d59a45;
    --ink: #3b2a1c;
    --bowl-rim: #5c6a73;
    --beans: #161312;
    --herb: #3f7a3a;
  }
  * { box-sizing: border-box; margin: 0; padding: 0; }
  html, body { width: 1200px; height: 800px; overflow: hidden; }
  body { background: var(--backdrop); position: relative; font-family: "Oswald", sans-serif; }

  .pouch {
    position: absolute; left: 380px; top: 40px; width: 440px; height: 720px;
    border-radius: 18px 18px 8px 8px;
    background:
      radial-gradient(ellipse at 50% 38%, var(--pouch-light) 0%, rgba(217,162,60,0) 60%),
      linear-gradient(180deg, var(--pouch-dark) 0%, var(--pouch-mid) 30%, var(--pouch-light) 60%, var(--pouch-mid) 100%);
    overflow: hidden;
  }
  .zip-line { position: absolute; left: 0; right: 0; top: 80px; height: 3px; background: rgba(90,50,20,.45); }
  .zip-line.second { top: 88px; height: 2px; }

  .ready-icon { position: absolute; left: 18px; top: 18px; width: 78px; height: 52px; }
  .ready-text { position: absolute; left: 26px; top: 24px; color: var(--gold); line-height: 1; }
  .ready-text small { display: block; font-size: 8px; letter-spacing: .5px; }
  .ready-text b { font-size: 17px; font-weight: 500; color: #f3e3c4; }
  .ready-text b span { font-size: 9px; }

  .brand-mark {
    position: absolute; top: 108px; left: 160px; width: 120px; height: 120px;
    border-radius: 50%; background: var(--band);
  }
  .brand-name {
    position: absolute; top: 240px; left: 0; right: 0; text-align: center;
    font-family: "Rye", serif; font-size: 34px; color: var(--band);
  }

  .bowl-photo {
    position: absolute; left: 55px; top: 380px; width: 330px; height: 270px;
    border-radius: 50%;
    border: 7px solid var(--bowl-rim);
    background:
      radial-gradient(circle at 62% 30%, rgba(63,122,58,.55) 0%, rgba(63,122,58,0) 22%),
      radial-gradient(circle at 35% 65%, rgba(63,122,58,.45) 0%, rgba(63,122,58,0) 18%),
      radial-gradient(ellipse at 50% 40%, #2d2623 0%, var(--beans) 75%);
  }

  .title-band { position: absolute; left: 0; top: 300px; width: 440px; height: 170px; }
  .product-title {
    position: absolute; top: 336px; left: 0; right: 0; text-align: center;
    font-family: "Rye", serif; font-size: 38px; color: var(--gold); letter-spacing: 1px;
  }
  .product-sub {
    position: absolute; top: 398px; left: 0; right: 0; text-align: center;
    font-size: 15px; color: var(--gold); letter-spacing: .5px;
  }

  .variety { position: absolute; top: 660px; left: 0; right: 0; text-align: center; color: var(--ink); line-height: 1.3; }
  .variety .spanish { font-family: "Rye", serif; font-size: 15px; }
  .variety .weight { font-size: 17px; font-weight: 500; }

  .oil-badge { position: absolute; right: 20px; top: 642px; width: 60px; height: 64px; }
</style>
</head>
<body>
  <div class="pouch">
    <div class="zip-line"></div>
    <div class="zip-line second"></div>

    <svg class="ready-icon" viewBox="0 0 78 52" aria-hidden="true">
      <rect x="2" y="2" width="74" height="48" rx="4" fill="none" stroke="#d59a45" stroke-width="3"/>
      <rect x="8" y="8" width="48" height="36" rx="2" fill="#3a2e27"/>
      <line x1="62" y1="10" x2="70" y2="10" stroke="#d59a45" stroke-width="2"/>
      <circle cx="66" cy="20" r="2" fill="#d59a45"/>
      <circle cx="66" cy="28" r="2" fill="#d59a45"/>
      <circle cx="66" cy="36" r="2" fill="#d59a45"/>
    </svg>
    <div class="ready-text"><small>Ready In</small><b>60<span>Sec</span></b></div>

    <div class="brand-mark"></div>
    <div class="brand-name">Brisk Harbor</div>

    <div class="bowl-photo" role="img" aria-label="Photo of a bowl of cooked black beans topped with chopped cilantro"></div>

    <svg class="title-band" viewBox="0 0 440 170" preserveAspectRatio="none" aria-hidden="true">
      <polygon fill="#2e2520" points="0,20 40,14 70,22 110,8 150,18 190,10 230,20 270,6 310,16 350,4 400,14 440,8 440,150 400,156 360,148 320,160 280,150 240,162 200,152 160,164 120,150 80,160 40,150 0,158"/>
    </svg>
    <div class="product-title">Ranger Black Beans</div>
    <div class="product-sub">★★★★ With Onions and Bell Papper ★★★★</div>

    <div class="variety">
      <div class="spanish">Frijolos Negros Cubanos</div>
      <div class="weight">NET WT. 10 OZ (283G)</div>
    </div>

    <svg class="oil-badge" viewBox="0 0 60 64" aria-hidden="true">
      <polygon points="30,2 58,19 58,62 2,62 2,19" fill="#c98a2e" stroke="#3a2e27" stroke-width="3"/>
      <polygon points="30,9 52,22 52,56 8,56 8,22" fill="#3a2e27" opacity=".25"/>
    </svg>
  </div>
</body>
</html>
```